TideLantern business card design

I would like a design that shows people that TideLantern is about using SOUND as a tool in ALL areas and stages of life - during labour, during motherhood, when a baby, child, adult at work, while sick, when dying, when celebrating.... there are MANY different pathways that the power of sound can be incorporated to help people relax, energise and connect with themselves and others.
The logo is purple...I can see pathways, swirling, colours, musical notes or sound waves.... white background on front. Can have different colour on back...I'm flexible and open to suggestions.

Target Market(s)

at the moment it is mostly expectant couples and mothers... but it really is for anyone who is looking for an alternative to "traditional" medicine

Industry/Entity Type

Adult

Contact Information for Business Card

Harriet Quenby - founder
0437162894
www.tidelantern.com.au
harriet@tidelantern.com.au
tidecradle
tidefrolic
tidenourishing
tidegatherings
tidekneading

Colors

Designer to choose colors to be used in the design.

Requirements
Must have
• logo
music notes/soundwaves - something that represents sound affecting people
something that represents pathways and/or connection

```html
<!DOCTYPE html>
<html lang="en">
<head>
<meta charset="utf-8">
<title>TideLantern business card</title>
<link href="https://fonts.googleapis.com/css2?family=Lato:wght@300;400;700&display=swap" rel="stylesheet">
<style>
  :root {
    --page: #e9e9ec;
    --card: #ffffff;
    --ink: #1c1c1c;
    --ink-soft: #333333;
    --purple: #9a3a9e;
    --purple-band: #8f2f93;
    --band-text: #ffffff;
    --art-light: #e4e4e4;
    --art-dark: #3a3a3a;
  }
  * { box-sizing: border-box; margin: 0; padding: 0; }
  html, body {
    width: 1200px; height: 926px; overflow: hidden;
    background: var(--page);
    font-family: "Lato", Arial, sans-serif;
  }
  .canvas {
    width: 1200px; height: 926px;
    display: flex; flex-direction: column;
    align-items: center; justify-content: center; gap: 40px;
  }
  .card {
    position: relative;
    width: 640px; height: 391px;
    background: var(--card);
    box-shadow: 0 6px 18px rgba(0,0,0,.14);
    overflow: hidden;
  }
  .brand-name {
    font-weight: 300;
    color: var(--purple);
    font-size: 60px;
    letter-spacing: -1px;
    line-height: 1;
    white-space: nowrap;
  }
  .tagline {
    font-weight: 400;
    color: var(--ink);
    font-size: 21px;
    letter-spacing: -.2px;
    margin-top: 12px;
    white-space: nowrap;
  }

  /* Contact side */
  .holder { position: absolute; left: 30px; top: 26px; }
  .holder-name { font-size: 24px; font-weight: 400; color: var(--ink); line-height: 1; }
  .holder-name strong { font-weight: 700; }
  .holder-role {
    font-size: 13px; color: var(--purple); letter-spacing: 1.5px;
    text-transform: uppercase; margin-top: 2px;
  }
  .contacts {
    position: absolute; left: 30px; top: 262px;
    list-style: none; color: var(--ink-soft);
  }
  .contacts li { display: flex; align-items: center; gap: 8px; font-size: 15px; line-height: 22px; }
  .contacts li.phone { font-size: 19px; }
  .contacts svg { width: 13px; height: 13px; fill: var(--purple); flex: none; }
  .contact-lockup { position: absolute; right: 30px; top: 150px; text-align: left; }
  .services {
    position: absolute; left: 0; right: 0; bottom: 0; height: 42px;
    background: var(--purple-band); color: var(--band-text);
    display: flex; align-items: center; padding-left: 30px;
    font-size: 11.5px; letter-spacing: 1px; text-transform: uppercase;
  }
  .services span + span::before { content: " - "; white-space: pre; }

  /* Logo side */
  .logo-lockup { position: absolute; left: 70px; top: 125px; }
  .note-art {
    position: absolute; right: 50px; top: 100px;
    width: 120px; height: 190px;
    background: radial-gradient(ellipse at 55% 78%, var(--art-dark) 0%, #8a8a8a 35%, var(--art-light) 65%, var(--card) 100%);
  }
</style>
</head>
<body>
<main class="canvas">
  <section class="card card--contact">
    <div class="holder">
      <p class="holder-name">Harriet <strong>Quenby</strong></p>
      <p class="holder-role">Founder</p>
    </div>
    <ul class="contacts">
      <li class="phone">
        <svg viewBox="0 0 16 16" aria-hidden="true"><path d="M2 3c0-1 1-2 2-2h1l2 3-1.5 1.5c.8 2 2.5 3.7 4.5 4.5L11.5 8.5l3 2v1c0 1-1 2-2 2C6.5 13.5 2 9 2 3z"/></svg>
        0437162894
      </li>
      <li>
        <svg viewBox="0 0 16 16" aria-hidden="true"><path d="M1 2h14v9H1zM3 4v5h10V4zM6 12h4v1h2v1H4v-1h2z"/></svg>
        tidelantern.com.au
      </li>
      <li>
        <svg viewBox="0 0 16 16" aria-hidden="true"><path d="M1 3h14v10H1zM2.5 4.5 8 9l5.5-4.5z"/></svg>
        harriet@tidelantern.com.au
      </li>
    </ul>
    <div class="contact-lockup">
      <p class="brand-name">TideLantern</p>
      <p class="tagline">calm for every season</p>
    </div>
    <div class="services">
      <span>tidecradle</span><span>tidefrolic</span><span>tidenourishing</span><span>tidegatherings</span><span>tidekneading</span>
    </div>
  </section>

  <section class="card card--logo">
    <div class="logo-lockup">
      <p class="brand-name">TideLantern</p>
      <p class="tagline">calm for every season</p>
    </div>
    <div class="note-art" role="img" aria-label="Dark music note dissolving into scattered particles"></div>
  </section>
</main>
</body>
</html>
```